Geschäftspapiere für Rechtsanwaltskanzlei
Zielgruppe
Rechtsanwaltskanzlei
Aufgabenstellung
Bitte inklusive Logo (sollte Recht, Digital/Apps, Medizin illustrieren) - habe das Preisgeld vor diesem Hintergrund erhöht.
Die Kanzlei arbeitet an der Schnittstelle von (Medizin-)Recht und Digital. Von daher wären wären Symbole/Gestaltung aus Bereich Medizin, Recht und Digital (z.B. Apps etc.) passend.
Das Briefpapier soll alle wichtigen Infos enthalten, aber dabei sehr klar gehalten werden und nicht überladen sein. Mir ist ein schlichtes und ansprechendes Design wichtig. Es soll nicht verspielt sein.
Info auf Briefpapier:
Kanzlei für Medizinrecht
Rechtsanwalt Dr. Tilman Brecke - Fachanwalt für Medizinrecht
Bitte Platzhalter/Freitextfelder für die anderen anderen Angaben, wie:
- Adresse
- Telefon-Nr.
- Homepage
- E-Mail
- Bankdaten.

```html
<!DOCTYPE html>
<html lang="de">
<head>
<meta charset="utf-8">
<title>Briefpapier – Kanzlei Dr. Tilman Brecke</title>
<link rel="stylesheet" href="https://fonts.googleapis.com/css2?family=Montserrat:wght@400;500;700&display=swap">
<style>
  :root {
    --backdrop: #e4e4e4;
    --paper: #ffffff;
    --ink: #5a5a5a;
    --ink-soft: #6e6e6e;
    --accent: #5b93b4;
  }
  * { box-sizing: border-box; margin: 0; padding: 0; }
  html, body {
    width: 1200px; height: 1105px; overflow: hidden;
    background: var(--backdrop);
    font-family: "Montserrat", sans-serif;
    color: var(--ink);
  }
  .letterhead {
    position: absolute; left: 232px; top: 30px;
    width: 736px; height: 1045px;
    background: var(--paper);
    box-shadow: 0 4px 18px rgba(0,0,0,.12);
  }
  .brand { position: absolute; left: 56px; top: 52px; }
  .brand-name {
    display: flex; align-items: center; gap: 12px;
    font-size: 30px; font-weight: 500; color: var(--ink);
    letter-spacing: .5px;
  }
  .brand-square { width: 16px; height: 16px; background: var(--ink); }
  .brand-firm {
    margin: 8px 0 0 28px;
    font-size: 13px; font-weight: 700; letter-spacing: 3px;
    color: var(--accent); text-transform: uppercase;
  }
  .brand-title { margin: 4px 0 0 28px; font-size: 14px; color: var(--ink-soft); }

  .contact {
    position: absolute; right: 40px; top: 120px;
    font-size: 9.5px; line-height: 1.45; color: var(--ink-soft);
  }
  .contact-address { margin-bottom: 8px; }
  .contact-row { display: flex; gap: 10px; }
  .contact-label { width: 30px; color: var(--accent); }
  .side-bar {
    position: absolute; right: 0; top: 128px;
    width: 14px; height: 110px; background: var(--accent);
  }
  .fold-mark {
    position: absolute; left: 28px; top: 370px;
    width: 14px; height: 1px; background: var(--ink-soft);
  }

  .footer {
    position: absolute; left: 48px; bottom: 84px;
    display: flex; align-items: flex-end; gap: 22px;
    font-size: 9.5px; line-height: 1.5; color: var(--ink-soft);
  }
  .footer-divider { width: 1px; height: 40px; background: var(--ink-soft); }
  .footer-label { color: var(--accent); }
  .bottom-band {
    position: absolute; left: 48px; right: 0; bottom: 66px;
    height: 7px; background: var(--accent);
  }
</style>
</head>
<body>
  <main class="letterhead">
    <header class="brand">
      <div class="brand-name"><span class="brand-square"></span>Dr. Tilman Brecke</div>
      <div class="brand-firm">Rechtsanwälte</div>
      <div class="brand-title">Fachanwalt für Medizinrecht</div>
    </header>

    <address class="contact" style="font-style:normal">
      <div class="contact-address">
        Lindenhofer Weg 8<br>
        16321 Kastelbruck<br>
        Ortsteil Heidmühl
      </div>
      <div class="contact-row"><span class="contact-label">Tel.</span>+49 000 000 47 3120</div>
      <div class="contact-row"><span class="contact-label">Fax.</span>+49 000 000 47 3121</div>
      <div class="contact-row"><span class="contact-label">Mail.</span>kontakt@kanzlei-brecke.de</div>
      <div class="contact-row"><span class="contact-label">Web.</span>www.kanzlei-brecke.de</div>
    </address>
    <div class="side-bar"></div>
    <div class="fold-mark"></div>

    <footer class="footer">
      <div class="footer-bank">
        <span class="footer-label">Bank:</span> Kreissparkasse Talheim<br>
        <span class="footer-label">IBAN:</span> DE XX 12345XX 0000004711<br>
        <span class="footer-label">BIC-Swift:</span> TALHDE21XXX
      </div>
      <div class="footer-divider"></div>
      <div class="footer-register">
        Amtsgericht Talheim<br>
        <span class="footer-label">Handelsregister:</span> 0000812<br>
        <span class="footer-label">USt.-ID-Nr.:</span> DE0008120000
      </div>
    </footer>
    <div class="bottom-band"></div>
  </main>
</body>
</html>
```